Plivoro ( A new twist on task management )

We need modern, elegant, and clean (Material Design) on screens, buttons, and icons.

It is a (smart) task management application which helps the users to get notified and track task completion hassle free; Using notification profiles they create.

The interface of this application should be very simple and color schemes should be contemporary as long as they don’t make reading short text hard.

Following Material Design guidelines, the prefered font style is Roboto
Updates

Target Market(s)

Everyone from 13+

Industry/Entity Type

Software

Logo Text

Plivoro

Font styles to use
Other font styles liked:
• Roboto

```html
<!DOCTYPE html>
<html lang="en">
<head>
<meta charset="utf-8">
<title>Plivoro – Active Tasks</title>
<link rel="stylesheet" href="https://fonts.googleapis.com/css2?family=Roboto:wght@300;400;500&display=swap">
<style>
  :root {
    --stage: #000000;
    --screen-bg: #f4f7f7;
    --header-red: #d3272e;
    --white: #ffffff;
    --ink: #333333;
    --icon-ink: #222222;
    --task-yellow: #fee417;
    --task-orange: #fdb718;
    --task-red: #ed1c24;
    --task-blue: #6dcff6;
  }
  * { margin: 0; padding: 0; box-sizing: border-box; }
  html, body { width: 1200px; height: 800px; overflow: hidden; background: var(--stage); }
  body { font-family: "Roboto", Arial, sans-serif; color: var(--ink); position: relative; }

  .screen {
    position: absolute; left: 397px; top: 40px; width: 406px; height: 721px;
    background: var(--screen-bg); overflow: hidden;
  }
  .status-bar {
    height: 21px; display: flex; align-items: center; justify-content: space-between;
    padding: 0 6px 0 7px; font-size: 11px; color: #111;
  }
  .status-bar .signal { display: flex; align-items: center; gap: 4px; }
  .status-bar .battery { display: flex; align-items: center; gap: 3px; }

  .app-header {
    height: 47px; background: var(--header-red); display: flex; align-items: center;
    padding: 0 16px 0 14px; color: var(--white);
  }
  .app-header .user-name { font-size: 18px; margin-left: 12px; flex: 1; }

  .page-title {
    height: 86px; background: var(--white); display: flex; align-items: center;
    justify-content: center; font-size: 17px; color: var(--ink);
  }

  .task {
    height: 66.5px; position: relative; display: flex;
  }
  .task--yellow { background: var(--task-yellow); }
  .task--orange { background: var(--task-orange); }
  .task--red { background: var(--task-red); }
  .task--blue { background: var(--task-blue); }

  .task .control { position: absolute; top: 22px; }
  .task .play { left: 27px; }
  .task .task-name { position: absolute; left: 72px; top: 12px; font-size: 19px; }
  .task .badges { position: absolute; right: 14px; top: 25px; display: flex; gap: 8px; align-items: center; }

  .task--active .stop { left: 27px; }
  .task--active .skip { left: 74px; }
  .task--active .task-info { position: absolute; left: 118px; top: 13px; font-size: 19px; line-height: 22px; }
  .task--active .timer { font-weight: 300; font-size: 18.5px; }
</style>
</head>
<body>
<main class="screen">
  <div class="status-bar">
    <span class="signal">
      <svg width="38" height="8" viewBox="0 0 38 8" aria-hidden="true"><g fill="#111"><circle cx="3" cy="4" r="3"/><circle cx="11" cy="4" r="3"/><circle cx="19" cy="4" r="3"/><circle cx="27" cy="4" r="3"/><circle cx="35" cy="4" r="3"/></g></svg>
      <svg width="13" height="10" viewBox="0 0 13 10" aria-hidden="true"><path d="M0.5 3.5a8.5 8.5 0 0 1 12 0M2.5 5.5a5.5 5.5 0 0 1 8 0" fill="none" stroke="#111" stroke-width="1.5"/><path d="M4.5 7.3a2.8 2.8 0 0 1 4 0L6.5 9.5z" fill="#111"/></svg>
    </span>
    <span class="clock">9:41 AM</span>
    <span class="battery">100%
      <svg width="27" height="11" viewBox="0 0 27 11" aria-hidden="true"><rect x="0.5" y="0.5" width="23" height="10" rx="2" fill="none" stroke="#111"/><rect x="2" y="2" width="20" height="7" fill="#111"/><rect x="24.5" y="3.5" width="2" height="4" fill="#111"/></svg>
    </span>
  </div>

  <header class="app-header">
    <svg width="28" height="28" viewBox="0 0 28 28" aria-hidden="true">
      <circle cx="14" cy="14" r="12.5" fill="none" stroke="#fff" stroke-width="2"/>
      <circle cx="14" cy="10.5" r="4.5" fill="#fff"/>
      <path d="M7.5 24c0-6 2.8-8.5 6.5-8.5s6.5 2.5 6.5 8.5z" fill="#fff"/>
    </svg>
    <span class="user-name">Jhon Doe</span>
    <svg width="24" height="17" viewBox="0 0 24 17" aria-label="Menu" role="img">
      <g fill="#fff"><rect x="0" y="1" width="2.5" height="2"/><rect x="4" y="1" width="20" height="2"/><rect x="0" y="7.5" width="2.5" height="2"/><rect x="4" y="7.5" width="20" height="2"/><rect x="0" y="14" width="2.5" height="2"/><rect x="4" y="14" width="20" height="2"/></g>
    </svg>
  </header>

  <h1 class="page-title" style="font-weight:400">Active Tasks</h1>

  <section class="task-list">
    <div class="task task--yellow">
      <svg class="control play" width="20" height="22" viewBox="0 0 20 22" aria-label="Start" role="img"><path d="M1 0l19 11L1 22z" fill="#fff"/></svg>
      <span class="task-name">Task 1</span>
      <span class="badges">
        <svg width="15" height="15" viewBox="0 0 15 15" aria-label="Pinned" role="img"><path d="M9 1l5 5-2 .5-3 3 .5 3-1.5 1.5-3-3L1.5 14.5 1 14l3.5-4-3-3L3 5.5l3 .5 3-3z" fill="#111"/></svg>
        <svg width="11" height="15" viewBox="0 0 11 15" aria-label="Location" role="img"><path d="M5.5 0.5a4.5 4.5 0 0 1 4.5 4.5c0 3-4.5 7-4.5 7S1 8 1 5a4.5 4.5 0 0 1 4.5-4.5z" fill="#333"/><circle cx="5.5" cy="5" r="1.7" fill="#ffe"/><rect x="1" y="12.5" width="9" height="2" rx="1" fill="#333"/></svg>
      </span>
    </div>

    <div class="task task--orange">
      <svg class="control play" width="20" height="22" viewBox="0 0 20 22" aria-label="Start" role="img"><path d="M1 0l19 11L1 22z" fill="#fff"/></svg>
      <span class="task-name">Task 2</span>
      <span class="badges">
        <svg width="15" height="15" viewBox="0 0 15 15" aria-label="Scheduled" role="img"><circle cx="7.5" cy="7.5" r="6.5" fill="none" stroke="#111" stroke-width="1.4"/><path d="M7.5 3.5v4l-2.5 2.5" fill="none" stroke="#111" stroke-width="1.4"/></svg>
        <svg width="11" height="15" viewBox="0 0 11 15" aria-label="Location" role="img"><path d="M5.5 0.5a4.5 4.5 0 0 1 4.5 4.5c0 3-4.5 7-4.5 7S1 8 1 5a4.5 4.5 0 0 1 4.5-4.5z" fill="#333"/><circle cx="5.5" cy="5" r="1.7" fill="#fdb718"/><rect x="1" y="12.5" width="9" height="2" rx="1" fill="#333"/></svg>
      </span>
    </div>

    <div class="task task--red">
      <svg class="control play" width="20" height="22" viewBox="0 0 20 22" aria-label="Start" role="img"><path d="M1 0l19 11L1 22z" fill="#fff"/></svg>
      <span class="task-name">Task 3</span>
      <span class="badges">
        <svg width="15" height="15" viewBox="0 0 15 15" aria-label="Scheduled" role="img"><circle cx="7.5" cy="7.5" r="6.5" fill="none" stroke="#111" stroke-width="1.4"/><path d="M7.5 3.5v4l-2.5 2.5" fill="none" stroke="#111" stroke-width="1.4"/></svg>
      </span>
    </div>

    <div class="task task--blue task--active">
      <svg class="control stop" width="21" height="21" viewBox="0 0 21 21" aria-label="Stop" role="img"><rect width="21" height="21" rx="3" fill="#fff"/></svg>
      <svg class="control skip" width="18" height="21" viewBox="0 0 18 21" aria-label="Next" role="img"><path d="M0 0l13 10.5L0 21z" fill="#fff"/><rect x="13" y="0" width="5" height="21" fill="#fff"/></svg>
      <div class="task-info">
        <div class="task-name-active">Task 4</div>
        <div class="timer">00h:15m:56s</div>
      </div>
      <span class="badges">
        <svg width="11" height="15" viewBox="0 0 11 15" aria-label="Location" role="img"><path d="M5.5 0.5a4.5 4.5 0 0 1 4.5 4.5c0 3-4.5 7-4.5 7S1 8 1 5a4.5 4.5 0 0 1 4.5-4.5z" fill="#333"/><circle cx="5.5" cy="5" r="1.7" fill="#6dcff6"/><rect x="1" y="12.5" width="9" height="2" rx="1" fill="#333"/></svg>
      </span>
    </div>
  </section>
</main>
</body>
</html>
```